I want a double sided flyer possibly with a picture of a lawn or grass.
Company name, phone number, email, and logo
Halvorsen Turf Management, (404)726-1853,Halvorsen_Turf@brevimail.com
Company services
Fertilization and weed control,Lawn and Landscape maintenance, mowing, pruning, aeration, landscape and Christmas lights,

```html
<!DOCTYPE html>
<html lang="en">
<head>
<meta charset="utf-8">
<title>Halvorsen Turf Management – Flyer</title>
<link href="https://fonts.googleapis.com/css2?family=PT+Sans+Narrow:wght@400;700&family=Open+Sans:wght@400;700&display=swap" rel="stylesheet">
<style>
  :root {
    --backdrop: #45d907;
    --brand-green: #3fb515;
    --deep-green: #1d6a0c;
    --dark-green: #0f3d06;
    --lime: #a8f03a;
    --sky-top: #4aa8e8;
    --sky-mid: #bfe1f7;
    --cream: #f3ead2;
    --ink: #1b1b1b;
    --white: #ffffff;
  }
  * { box-sizing: border-box; margin: 0; padding: 0; }
  html, body { width: 1200px; height: 932px; overflow: hidden; }
  body { background: var(--backdrop); position: relative; font-family: "Open Sans", sans-serif; }

  .flyer-side { position: absolute; width: 530px; height: 752px; overflow: hidden; }

  /* Front side */
  .front { left: 72px; top: 23px;
    background: linear-gradient(180deg, var(--sky-top) 0%, var(--sky-mid) 18%, #f4f9fd 40%, #e9f5ee 55%, #cfeab0 70%); }
  .front .brand-mark { position: absolute; left: 80px; top: 62px; width: 78px; height: 78px; border-radius: 50%; background: var(--brand-green); }
  .front .brand-name { position: absolute; left: 178px; top: 64px; width: 300px;
    font-family: "PT Sans Narrow", sans-serif; font-weight: 700; font-size: 34px; line-height: 38px; color: var(--brand-green); }
  .service-list { position: absolute; left: 212px; top: 172px; list-style: none; }
  .service-list li { position: relative; height: 33px; width: 187px; padding-left: 36px;
    font-family: "PT Sans Narrow", sans-serif; font-size: 18px; line-height: 26px; color: var(--ink);
    border-bottom: 1px dotted #8a8a8a; white-space: nowrap; }
  .service-list li::before { content: ""; position: absolute; left: 2px; top: 5px; width: 18px; height: 18px; border-radius: 50%; background: var(--brand-green); }
  .front .yard-scene { position: absolute; left: 0; top: 330px; width: 530px; height: 340px;
    background: linear-gradient(180deg, rgba(200,235,160,0) 0%, #b9e38a 30%, #6cc43a 65%, #3a8f1c 100%); }
  .front .footer-band { position: absolute; left: 0; bottom: 0; width: 530px; height: 130px; }
  .front .footer-name { position: absolute; left: 0; top: 666px; width: 530px; text-align: center;
    font-weight: 700; font-size: 21px; color: var(--white); }
  .front .contact-line { position: absolute; top: 700px; display: flex; align-items: center; gap: 8px;
    font-family: "PT Sans Narrow", sans-serif; font-size: 21px; color: var(--white); }
  .front .contact-phone { left: 34px; }
  .front .contact-email { left: 256px; }

  /* Back side */
  .back { left: 626px; top: 157px; height: 753px;
    background: linear-gradient(180deg, #b9f046 0%, #5fcc1e 22%, #1f7a0d 45%, var(--dark-green) 62%, #2a8a10 78%, var(--lime) 100%); }
  .back .brand-mark { position: absolute; left: 215px; top: 90px; width: 100px; height: 100px; border-radius: 50%; background: var(--cream); }
  .back .brand-name { position: absolute; left: 0; top: 226px; width: 530px; text-align: center;
    font-family: "PT Sans Narrow", sans-serif; font-weight: 700; font-size: 46px; line-height: 50px; color: var(--cream); }
  .back .contact-icon { position: absolute; left: 253px; }
  .back .contact-text { position: absolute; left: 0; width: 530px; text-align: center; font-weight: 700; color: var(--cream); }
  .back .phone-icon { top: 395px; }
  .back .phone-text { top: 428px; font-size: 30px; }
  .back .mail-icon { top: 480px; }
  .back .email-text { top: 510px; font-size: 28px; }
  .back .crew-scene { position: absolute; left: 0; bottom: 0; width: 530px; height: 210px;
    background: linear-gradient(180deg, rgba(120,210,60,0) 0%, #6bd02a 40%, #9fee3e 80%, var(--lime) 100%); }
</style>
</head>
<body>

<section class="flyer-side front">
  <div class="brand-mark"></div>
  <div class="brand-name">Halvorsen Turf Management</div>

  <ul class="service-list">
    <li>Fertilization &amp; Weed control</li>
    <li>Lawn &amp; Landscape Maintenance</li>
    <li>Mowing</li>
    <li>Pruning</li>
    <li>Aeration</li>
    <li>Landscape &amp; Christmas Lights</li>
  </ul>

  <div class="yard-scene" role="img" aria-label="Photo of a house with a green lawn and trees, with silhouetted gardeners mowing, raking, pruning from a ladder and pushing a wheelbarrow"></div>

  <svg class="footer-band" viewBox="0 0 530 130" aria-hidden="true">
    <path d="M0 22 Q270 40 530 0 L530 130 L0 130 Z" fill="#3fb515"/>
    <path d="M0 18 Q270 36 530 -4" fill="none" stroke="#ffffff" stroke-width="3"/>
  </svg>

  <div class="footer-name">Halvorsen Turf Management</div>
  <div class="contact-line contact-phone">
    <svg width="22" height="16" viewBox="0 0 22 16" aria-hidden="true"><path d="M1 6 Q11 -2 21 6 L18 8 L15 5 L7 5 L4 8 Z M5 9 L17 9 L19 15 L3 15 Z" fill="#fff"/></svg>
    <span>(404)726-1853</span>
  </div>
  <div class="contact-line contact-email">
    <svg width="24" height="16" viewBox="0 0 24 16" aria-hidden="true"><rect x="1" y="1" width="22" height="14" fill="none" stroke="#fff" stroke-width="2"/><path d="M1 1 L12 9 L23 1" fill="none" stroke="#fff" stroke-width="2"/></svg>
    <span>Halvorsen_Turf@brevimail.com</span>
  </div>
</section>

<section class="flyer-side back">
  <div class="brand-mark"></div>
  <div class="brand-name">Halvorsen<br>Turf Management</div>

  <svg class="contact-icon phone-icon" width="24" height="18" viewBox="0 0 22 16" aria-hidden="true"><path d="M1 6 Q11 -2 21 6 L18 8 L15 5 L7 5 L4 8 Z M5 9 L17 9 L19 15 L3 15 Z" fill="#f3ead2"/></svg>
  <div class="contact-text phone-text">(404)726-1853</div>

  <svg class="contact-icon mail-icon" width="24" height="16" viewBox="0 0 24 16" aria-hidden="true"><rect x="1" y="1" width="22" height="14" fill="none" stroke="#f3ead2" stroke-width="2"/><path d="M1 1 L12 9 L23 1" fill="none" stroke="#f3ead2" stroke-width="2"/></svg>
  <div class="contact-text email-text">Halvorsen_Turf@brevimail.com</div>

  <div class="crew-scene" role="img" aria-label="Silhouettes of lawn care workers mowing, raking, planting, pushing a wheelbarrow and trimming trees from a ladder in a green park"></div>
</section>

</body>
</html>
```